依頼詳細
オンライン旅行イベントのチラシです。ターゲット層は特にありません。詳細は添付ファイルにラフなどを入れてますので、ご確認頂ければ幸いです。
記載項目
日時、申し込み方法、費用(無料)、視聴方法など
サイズ
A4
ページ数
両面
希望イメージ
シンプル 複雑
単色 カラフル
暗い 明るい
日常 高級
遊び心 厳粛
未来的 伝統的
女性的 男性的
希望する色
設定なし
納品ファイル
• イラストレーター形式 (.ai)
補足説明
最終的にこちらで修正を入れますので、アウトラインはかけていない状態で納品をお願いします

```html
<!DOCTYPE html>
<html lang="ja">
<head>
<meta charset="utf-8">
<title>お買い物オンラインツアー 東京の魅力発見</title>
<link href="https://fonts.googleapis.com/css2?family=Noto+Sans+JP:wght@400;500;700;900&family=Noto+Serif+JP:wght@700;900&display=swap" rel="stylesheet">
<style>
:root{
  --red:#e2231a;
  --orange:#f0642a;
  --ink:#1d1d1d;
  --green:#1e8a3c;
  --blue:#1f5fb4;
  --white:#ffffff;
  --paper:#ffffff;
}
*{margin:0;padding:0;box-sizing:border-box}
html,body{width:849px;height:1200px;overflow:hidden;background:var(--paper)}
body{font-family:"Noto Sans JP",sans-serif;color:var(--ink)}
.flyer{position:relative;width:849px;height:1200px;overflow:hidden;background:var(--paper)}
.abs{position:absolute}
.hero-photo{left:420px;top:0;width:429px;height:260px;background:linear-gradient(135deg,#e7d9c9,#b98a6c 55%,#6d4a3a);border-bottom-left-radius:160px 120px}
.swoosh{left:0;top:0;width:849px;height:900px}
.kicker{left:70px;top:22px;font-size:38px;font-weight:700;line-height:1.2;color:var(--ink);font-family:"Noto Serif JP",serif}
.title{left:120px;top:100px;font-size:150px;font-weight:900;line-height:1;color:var(--red);font-family:"Noto Serif JP",serif;letter-spacing:4px;-webkit-text-stroke:4px var(--white);paint-order:stroke fill}
.subtitle{left:330px;top:262px;font-size:42px;font-weight:900;font-family:"Noto Serif JP",serif;color:var(--ink)}
.temple-photo{left:170px;top:320px;width:679px;height:530px;background:linear-gradient(180deg,#9cc3e8 0%,#c9dcee 30%,#b2372c 55%,#6b2a24 80%,#4a4a4a 100%)}
.food-photo{left:30px;top:440px;width:260px;height:260px;border-radius:50%;border:6px solid var(--white);background:radial-gradient(circle,#a86a2c,#5a3114 70%,#2b1a10);box-shadow:0 4px 10px rgba(0,0,0,.3)}
.snack-photo{left:30px;top:720px;width:150px;height:110px;border:5px solid var(--white);background:linear-gradient(135deg,#d8b27a,#8a5a2e);box-shadow:0 3px 8px rgba(0,0,0,.3)}
.schedule{left:40px;top:868px;width:790px}
.row{display:flex;align-items:center;height:44px;margin-bottom:8px}
.tag{background:var(--green);color:var(--white);font-weight:700;font-size:20px;padding:4px 16px;width:230px;font-family:"Noto Serif JP",serif}
.date{margin-left:30px;color:var(--red);font-weight:900;font-size:30px;display:flex;align-items:center}
.date .md{font-size:38px;margin-left:4px}
.day{display:inline-block;color:var(--white);font-size:22px;width:34px;height:34px;line-height:34px;text-align:center;margin:0 14px 0 8px}
.day.mon{background:var(--red);border-radius:50%}
.day.sat{background:var(--blue)}
.time{color:var(--ink);font-size:26px;font-weight:700}
.free{left:20px;top:975px;width:410px;height:165px;background:var(--red);color:var(--white);padding:10px 16px}
.free h2{font-size:30px;font-weight:900;line-height:1.1}
.free .method{font-size:18px;font-weight:700;margin:4px 0 6px}
.free p{font-size:10.5px;line-height:1.55}
.apply{left:450px;top:978px;width:380px;font-weight:700;font-size:15px;line-height:1.6}
.apply .url{margin-top:4px}
.qr{left:716px;top:1050px;width:92px;height:88px;background:#9a9a9a}
.qr-label{left:640px;top:1082px;font-size:11px;font-weight:700}
.footer{left:20px;top:1150px;width:810px;font-size:10px;line-height:1.5;color:var(--ink)}
</style>
</head>
<body>
<div class="flyer">
  <div class="abs hero-photo" role="img" aria-label="着物姿で東京の街を散策する二人の女性の写真"></div>
  <svg class="abs swoosh" viewBox="0 0 849 900" aria-hidden="true">
    <circle cx="140" cy="200" r="150" fill="var(--orange)"/>
    <path d="M0 330 C120 300 220 320 330 360 L330 390 C220 360 110 350 0 380 Z" fill="var(--red)"/>
    <path d="M0 260 C60 300 130 330 200 330 L170 420 L0 420 Z" fill="var(--orange)" opacity=".85"/>
  </svg>
  <div class="abs kicker">お買い物<br>オンラインツアー</div>
  <div class="abs title">東京</div>
  <div class="abs subtitle">の魅力発見!!</div>
  <div class="abs temple-photo" role="img" aria-label="浅草の朱塗りの寺院の門と参拝客の写真"></div>
  <div class="abs food-photo" role="img" aria-label="串焼きの名物料理の写真"></div>
  <div class="abs snack-photo" role="img" aria-label="店頭に並ぶ和菓子の写真"></div>

  <div class="abs schedule">
    <div class="row">
      <span class="tag">第一弾 ~禅トリップ~</span>
      <span class="date">2021年<span class="md">7/20</span><span class="day mon">月</span></span>
      <span class="time">12:00~13:00</span>
    </div>
    <div class="row">
      <span class="tag">第二弾 ~食トリップ~</span>
      <span class="date">2021年<span class="md">7/31</span><span class="day sat">土</span></span>
      <span class="time">13:00~14:00</span>
    </div>
  </div>

  <div class="abs free">
    <h2>視聴無料!!</h2>
    <div class="method">視聴方法：オンライン配信</div>
    <p>※お申し込み後、ご登録のメールアドレスへ視聴用URLをお送りします。<br>※配信中の商品はその場でご購入いただけます。<br>※通信環境の良い場所でのご視聴をおすすめいたします。</p>
  </div>

  <div class="abs apply">
    申し込み方法：Tixora からのお申し込みとなります。
    <div class="url">URL：https://www.tixora.jp/tokyo-tour</div>
  </div>
  <div class="abs qr-label">QRコードは<br>こちら</div>
  <div class="abs qr" role="img" aria-label="申し込みページのQRコード"></div>

  <div class="abs footer">主催：さくら観光協会　協力：株式会社ミナト旅行、株式会社ハナビ・ジャパン<br>後援：株式会社ソラ観光、株式会社ユメ交通、株式会社ツバサ企画</div>
</div>
</body>
</html>
```